Website Design for The Lamp Yard (Online Furniture Retailer)

Complete redesign of furniture commerce website using the latest trends. Blank canvas to work with!

```html
<!DOCTYPE html>
<html lang="en">
<head>
<meta charset="utf-8">
<title>The Lamp Yard</title>
<link href="https://fonts.googleapis.com/css2?family=Marcellus&family=Raleway:wght@300;400&family=Fauna+One&family=Open+Sans:wght@400;600&display=swap" rel="stylesheet">
<style>
:root{
  --pink:#e3187c;
  --deep-pink:#c4145f;
  --darker-pink:#a80f50;
  --frame:#4a4a4a;
  --side:#efefef;
  --line:#e2e2e2;
  --nav:#8a8a8a;
  --text:#3d3d3d;
  --white:#ffffff;
  --caption:rgba(40,40,40,.82);
}
*{margin:0;padding:0;box-sizing:border-box}
html,body{width:973px;height:1200px;overflow:hidden;background:var(--white)}
.page{position:relative;width:973px;height:1200px;background:var(--white);font-family:"Raleway",sans-serif}
.frame-left{position:absolute;left:0;top:0;width:26px;height:1200px;background:var(--frame)}
.frame-right{position:absolute;right:0;top:0;width:6px;height:1200px;background:var(--frame)}
.sidebar{position:absolute;left:26px;top:0;width:125px;height:732px;background:var(--side)}
.sidebar-low{position:absolute;left:26px;top:944px;width:124px;height:256px;background:var(--side)}
.brand{position:absolute;left:26px;top:30px;width:142px;height:67px;background:var(--pink);color:var(--white);font-family:"Marcellus",serif;font-size:27px;line-height:30px;padding:4px 0 0 11px}
.brand-fold{position:absolute;left:150px;top:97px}
.top-links{position:absolute;top:9px;right:127px;font-size:13px;color:var(--nav);font-family:"Raleway",sans-serif}
.top-links span.sep{color:var(--pink);margin:0 6px}
.top-links .active{color:var(--pink)}
.main-nav{position:absolute;top:58px;left:176px;width:670px;display:flex;justify-content:space-between;font-size:14px;font-weight:300;color:var(--nav)}
.main-nav .active{color:var(--pink)}
.cat-list{position:absolute;left:26px;top:137px;width:125px;list-style:none;font-size:12.5px}
.cat-list li{height:28.7px;line-height:28px;padding-left:16px;color:#9a9a9a;border-bottom:1px solid var(--line)}
.cat-list li.open{color:var(--pink);font-size:13px}
.cat-list li.sub{padding-left:30px;color:var(--text)}
.social{position:absolute;left:5px;top:593px}
.social i{display:block;width:16px;height:16px;border-radius:50%;background:#d8d8d8;margin-bottom:4px}
.social i.on{background:var(--white)}
.tip{position:absolute;left:30px;top:592px;border:1px solid #9a9a9a;background:var(--white);font-size:11px;padding:2px 9px;color:var(--text);font-family:"Open Sans",sans-serif}
.hero{position:absolute;left:169px;top:85px;width:676px;height:384px;background:linear-gradient(90deg,#e9dfd6 0%,#d9b9a8 30%,#9c2f28 55%,#8e2a24 100%);border:1px solid #ccc}
.hero-floor{position:absolute;left:0;bottom:0;width:100%;height:45%;background:linear-gradient(180deg,#efe5dc,#e3cbb5)}
.marker{position:absolute;width:17px;height:17px}
.price-tag{position:absolute;left:160px;top:264px;background:var(--white);border:1px solid #ddd;font-size:10px;color:var(--pink);padding:2px 8px;font-family:"Open Sans",sans-serif}
.hero-arrow{position:absolute;top:185px;width:14px;height:14px;background:#e8e8e8;border:1px solid #bbb}
h2{font-family:"Marcellus",serif;font-weight:400}
.popular-title{position:absolute;left:167px;top:490px;font-size:23px;color:var(--deep-pink)}
.toggles{position:absolute}
.thumbs{position:absolute;left:169px;top:526px;width:678px;display:grid;grid-template-columns:repeat(6,97px);column-gap:19.2px;row-gap:18px}
.thumb{height:85px;border:1px solid #c9c9c9;background:linear-gradient(160deg,#ffffff 30%,#d7264f 60%,#f0e3cc 100%)}
.thumb.b{background:linear-gradient(180deg,#ffffff 25%,#c8203e 55%,#ead8b8 80%,#ffffff 100%)}
.recommend{position:absolute;left:150px;top:732px;width:817px;height:212px;background:var(--deep-pink)}
.rec-head{position:absolute;left:150px;top:732px}
.rec-title{position:absolute;left:169px;top:768px;font-size:23px;color:var(--white)}
.rec-text{position:absolute;left:169px;top:810px;width:308px;font-family:"Fauna One",serif;font-size:9.6px;line-height:15.6px;color:#f7cfe0}
.photo{position:absolute;left:508px;width:337px}
.photo-a{top:732px;height:212px;background:linear-gradient(180deg,#c9c9c7 0%,#e6e6e4 50%,#8d8b88 100%)}
.photo-b{top:947px;height:210px;background:linear-gradient(180deg,#efe9e4 0%,#e0d6cf 35%,#d4264c 55%,#c21f43 75%,#d9cfc3 100%)}
.caption{position:absolute;left:0;bottom:0;width:100%;height:28px;background:var(--caption);color:var(--white);font-family:"Open Sans",sans-serif;font-size:10.5px;font-weight:600;padding:7px 11px;display:flex;justify-content:space-between}
.caption .more{font-weight:400;font-size:9.5px;letter-spacing:.5px}
.caption .more b{color:var(--pink);margin-left:8px}
.about-title{position:absolute;left:169px;top:956px;font-size:23px;color:var(--deep-pink)}
.about-text{position:absolute;left:169px;top:1000px;width:314px;font-family:"Fauna One",serif;font-size:9.6px;line-height:15.4px;color:var(--text);text-align:justify}
.footer-copy{position:absolute;left:168px;top:1176px;font-size:10px;color:var(--text);font-family:"Open Sans",sans-serif}
.footer-copy span{color:var(--deep-pink)}
.footer-nav{position:absolute;right:127px;top:1177px;display:flex;gap:21px;font-size:9.5px;color:var(--text);font-family:"Open Sans",sans-serif}
</style>
</head>
<body>
<div class="page">
  <div class="frame-left"></div>
  <div class="frame-right"></div>
  <div class="sidebar"></div>
  <div class="sidebar-low"></div>

  <div class="brand">The Lamp<br>Yard</div>
  <svg class="brand-fold" width="18" height="14"><polygon points="0,0 18,0 0,14" fill="#a80f50"/></svg>

  <nav class="top-links">My Account<span class="sep">/</span>My Shopping<span class="sep">/</span><span class="active">Checkout</span><span class="sep">/</span>Contact Us<span class="sep">/</span>Site Map</nav>

  <nav class="main-nav">
    <span>Overview</span><span>Store &amp; Showroom</span><span class="active">Testimonials</span><span>Delivery &amp;Returns</span><span>Privacy Notice</span><span>Terms &amp; Conditions</span>
  </nav>

  <ul class="cat-list">
    <li class="open">Headboards</li>
    <li class="sub">Faux Leather</li>
    <li class="sub">Leather</li>
    <li class="sub">Metal</li>
    <li class="sub">Wooden</li>
    <li>Kids Range</li>
    <li>Leather Beads</li>
    <li>Mattresses</li>
    <li>Metal Beds</li>
    <li>Novelty Beds</li>
    <li>Oak Beds</li>
    <li>Ottoman Beds</li>
    <li>Pet Beds</li>
  </ul>

  <div class="social"><i class="on"></i><i></i><i></i></div>
  <div class="tip">Pinecone</div>

  <div class="hero" role="img" aria-label="Bedroom with a low wooden bed, white bedding, red feature wall and tall window with red curtains">
    <div class="hero-floor"></div>
    <svg class="marker" style="left:94px;top:236px" viewBox="0 0 17 17"><circle cx="8.5" cy="8.5" r="8.5" fill="#111"/><path d="M8.5 4v9M4 8.5h9" stroke="#fff" stroke-width="2"/></svg>
    <svg class="marker" style="left:188px;top:288px" viewBox="0 0 17 17"><circle cx="8.5" cy="8.5" r="8.5" fill="#888"/><path d="M8.5 4v9M4 8.5h9" stroke="#fff" stroke-width="2"/></svg>
    <svg class="marker" style="left:349px;top:283px" viewBox="0 0 17 17"><circle cx="8.5" cy="8.5" r="8.5" fill="#111"/><path d="M8.5 4v9M4 8.5h9" stroke="#fff" stroke-width="2"/></svg>
    <svg class="marker" style="left:594px;top:246px" viewBox="0 0 17 17"><circle cx="8.5" cy="8.5" r="8.5" fill="#111"/><path d="M8.5 4v9M4 8.5h9" stroke="#fff" stroke-width="2"/></svg>
    <div class="price-tag">Bed Frame &nbsp;150$ &nbsp;&#9656;</div>
    <div class="hero-arrow" style="left:-1px"></div>
    <div class="hero-arrow" style="right:-1px"></div>
  </div>

  <h2 class="popular-title">Popular Categories</h2>
  <svg class="toggles" style="left:786px;top:500px" width="42" height="12"><polygon points="0,1 16,1 8,10" fill="#c4145f"/><polygon points="26,10 42,10 34,1" fill="#c4145f"/></svg>

  <div class="thumbs" role="img" aria-label="Product thumbnails of red lounge chairs and round upholstered footstools">
    <div class="thumb"></div><div class="thumb b"></div><div class="thumb"></div><div class="thumb b"></div><div class="thumb"></div><div class="thumb b"></div>
    <div class="thumb b"></div><div class="thumb"></div><div class="thumb b"></div><div class="thumb"></div><div class="thumb b"></div><div class="thumb"></div>
  </div>

  <div class="recommend"></div>
  <svg class="rec-head" width="358" height="32"><polygon points="0,0 358,0 358,10 0,32" fill="#a80f50"/><polygon points="0,0 28,0 0,14" fill="#8c0c42"/></svg>
  <h2 class="rec-title">We Recommend</h2>
  <svg class="toggles" style="left:440px;top:760px" width="40" height="11"><polygon points="0,1 15,1 7.5,10" fill="#fff"/><polygon points="25,10 40,10 32.5,1" fill="#fff"/></svg>
  <p class="rec-text">There are many variations of passages of Lorem Ipsum available, but the majority have suffered alteration in some form, by injected humour, or randomised words which don't look even slightly believable. If you are going to use a passage of Lorem Ipsum, you need to be sure there isn't anything embarrassing hidden in the middle of text. All the Lorem Ipsum generators on the Internet tend to repeat predefined chunks as necessary, making this the first true</p>

  <div class="photo photo-a" role="img" aria-label="Bright modern bedroom with a white bed, wooden side chests and a large window">
    <div class="caption"><span>Lorem Ipsum » Dolor</span><span class="more">MORE<b>•</b></span></div>
  </div>

  <h2 class="about-title">About The Lamp Yard</h2>
  <p class="about-text">Contrary to popular belief, Lorem Ipsum is not simply random text. It has roots in a piece of classical Latin literature from 45 BC, making it over 2000 years old. Edwin Harrow, a Latin professor at Ashford College in Vermont, looked up one of the more obscure Latin words, consectetur, from a Lorem Ipsum passage, and going through the cites of the word in classical literature, discovered the undoubtable source. Lorem Ipsum comes from sections 1.10.32 and 1.10.33 of "de Finibus Bonorum et Malorum" (The Extremes of</p>

  <div class="photo photo-b" role="img" aria-label="Red two-seat sofa with cushions in a light room">
    <div class="caption"><span>Lorem Ipsum » Dolor</span><span class="more">MORE<b>•</b></span></div>
  </div>

  <p class="footer-copy"><span>Marlow Furniture Limited</span> - Copyright © 2011</p>
  <nav class="footer-nav"><span>Home</span><span>About Us</span><span>Products</span><span>Customer Service</span><span>Contact Us</span></nav>
</div>
</body>
</html>
```